Business Card for High End Car Audio Company

Need a new bold business cards with our colors (blue, black, white, silver) and logo's. The card needs to have a high end look and would like the logo to be a large focus if possible. I've included old card for reference. The look was a little too simple for us. Needs nice double sided card.

Our company is a high end car audio company that produces subwoofers, speakers, and amplifiers for cars.

Target Market(s)

Car Audio

Industry/Entity Type

Electronic

Contact Information for Business Card

I included old business card for reference. Will need a template so I can use to create several cards for different people and departments.

Font styles to use
Serif
Sans Serif
Script

Colors
0555a3
ffffff
000000
9d9d9d

Requirements
Must have
• Logo, Info, Colors
Nice to have
• Bold and Elegant Design
Should not have
• Should not be plain.

```html
<!DOCTYPE html>
<html lang="en">
<head>
<meta charset="utf-8">
<title>Voltrane Audio – Business Card</title>
<link href="https://fonts.googleapis.com/css2?family=Open+Sans:wght@400;600;700&display=swap" rel="stylesheet">
<style>
  :root {
    --stage: #2a2c30;
    --card-black: #1b1c1e;
    --card-black-edge: #111213;
    --brand-blue: #0555a3;
    --blue-deep: #0a3f86;
    --blue-bright: #1e8fd6;
    --blue-line: #2fa3ea;
    --silver: #9d9d9d;
    --silver-light: #d4d6d9;
    --white: #ffffff;
  }
  * { margin: 0; padding: 0; box-sizing: border-box; }
  html, body {
    width: 1200px; height: 1200px; overflow: hidden;
    background: var(--stage);
    font-family: "Open Sans", Arial, sans-serif;
  }
  .sheet {
    width: 1200px; height: 1200px;
    display: flex; flex-direction: column; align-items: center; justify-content: center;
    gap: 60px;
  }
  .card {
    position: relative;
    width: 900px; height: 514px;
    overflow: hidden;
    box-shadow: 0 18px 40px rgba(0,0,0,.45);
  }

  /* Back side */
  .card-back {
    background: linear-gradient(135deg, var(--card-black) 0%, var(--card-black-edge) 100%);
  }
  .card-back .glow {
    position: absolute; left: -120px; top: 40px; width: 520px; height: 520px;
    border-radius: 50%;
    background: radial-gradient(circle, rgba(30,143,214,.18) 0%, rgba(30,143,214,0) 70%);
  }
  .wordmark {
    position: absolute;
    display: flex; align-items: center; gap: 22px;
    font-weight: 700; color: var(--blue-bright);
    text-transform: uppercase; letter-spacing: 4px; line-height: 1;
  }
  .wordmark .dot {
    border-radius: 50%; background: var(--blue-bright); flex: none;
  }
  .card-back .wordmark { left: 190px; top: 200px; font-size: 64px; }
  .card-back .wordmark .dot { width: 70px; height: 70px; }
  .wordmark .lines { display: flex; flex-direction: column; gap: 10px; }
  .wordmark .sub { padding-left: 160px; }

  /* Front side */
  .card-front {
    background: linear-gradient(120deg, var(--blue-deep) 0%, var(--brand-blue) 45%, var(--blue-bright) 100%);
    color: var(--white);
  }
  .card-front .glow {
    position: absolute; right: -60px; top: 20px; width: 420px; height: 420px; border-radius: 50%;
    background: radial-gradient(circle, rgba(255,255,255,.12) 0%, rgba(255,255,255,0) 70%);
  }
  .card-front .wordmark { left: 60px; top: 60px; font-size: 40px; color: var(--silver-light); gap: 0; }
  .card-front .wordmark .sub { padding-left: 100px; }

  .contact { position: absolute; left: 60px; top: 215px; }
  .contact .name { font-size: 36px; font-weight: 700; line-height: 1.1; }
  .contact .title { font-size: 19px; margin-top: 2px; }
  .contact .address { font-size: 19px; line-height: 1.3; margin-top: 26px; }
  .contact .links { list-style: none; margin-top: 20px; font-size: 19px; line-height: 1.45; }
  .contact .links li { display: flex; align-items: center; gap: 10px; }
  .contact .links svg { width: 16px; height: 16px; flex: none; }

  .bands { position: absolute; left: 0; right: 0; bottom: 0; height: 56px; }
  .bands .line-top { height: 4px; background: var(--blue-line); }
  .bands .silver { height: 24px; background: linear-gradient(90deg, var(--silver) 0%, var(--silver-light) 60%, var(--silver) 100%); }
  .bands .line-mid { height: 6px; background: var(--blue-line); }
  .bands .base { height: 22px; background: var(--blue-deep); }
</style>
</head>
<body>
<main class="sheet">
  <section class="card card-back" aria-label="Card back">
    <div class="glow"></div>
    <div class="wordmark">
      <span class="dot"></span>
      <span class="lines"><span>Voltrane</span><span class="sub">Audio</span></span>
    </div>
  </section>

  <section class="card card-front" aria-label="Card front">
    <div class="glow"></div>
    <div class="wordmark">
      <span class="lines"><span>Voltrane</span><span class="sub">Audio</span></span>
    </div>
    <div class="contact">
      <p class="name">Marcus Hale</p>
      <p class="title">CEO &amp; President</p>
      <p class="address">4820 Route 19<br>Fairview, TN 37062</p>
      <ul class="links">
        <li>
          <svg viewBox="0 0 16 16" aria-hidden="true"><path fill="#fff" d="M4 1l2.5 3-1.4 1.6c.8 1.9 2.3 3.4 4.2 4.3L11 8.5l3 2.5-1.6 2.7C7 13.2 2.6 8.8 1.3 3.6z"/></svg>
          1.555.203.4417
        </li>
        <li>
          <svg viewBox="0 0 16 16" aria-hidden="true"><rect x="1" y="3" width="14" height="10" fill="#fff"/><path d="M1 3l7 6 7-6" fill="none" stroke="#0a3f86" stroke-width="1.4"/></svg>
          info@voltraneaudio.com
        </li>
        <li>
          <svg viewBox="0 0 16 16" aria-hidden="true" fill="none" stroke="#fff" stroke-width="1.2"><circle cx="8" cy="8" r="6.5"/><ellipse cx="8" cy="8" rx="3" ry="6.5"/><path d="M1.5 8h13M2.5 5h11M2.5 11h11"/></svg>
          www.voltraneaudio.com
        </li>
      </ul>
    </div>
    <div class="bands">
      <div class="line-top"></div>
      <div class="silver"></div>
      <div class="line-mid"></div>
      <div class="base"></div>
    </div>
  </section>
</main>
</body>
</html>
```